Web app with questionnaires and graphs

For crewlifters.nl I want a clean design with good UX . It's a web app that let's users fill in questionnaires to assess things like team culture, psychological safety and so on. Colorwise should work with the Velkor Institute green logo. The app displays graphs (bar, line, pie) so these should also be incorporated.

```html
<!DOCTYPE html>
<html lang="en">
<head>
<meta charset="utf-8">
<title>Crewlifters – team tools</title>
<link href="https://fonts.googleapis.com/css2?family=Roboto:wght@400;500;700&display=swap" rel="stylesheet">
<style>
:root{
  --green:#0cbf2f;
  --green-soft:#d6f5dc;
  --green-mid:#8fe3a0;
  --ink:#1d1d1f;
  --muted:#6b6b72;
  --faint:#9a9aa2;
  --page:#f3f3f6;
  --canvas:#e6e6e6;
  --card:#ffffff;
  --field:#efeff3;
  --footer:#222325;
  --tab-off:#8c8c8c;
}
*{box-sizing:border-box;margin:0;padding:0}
html,body{width:1200px;height:1184px;overflow:hidden}
body{background:var(--canvas);font-family:'Roboto',Arial,sans-serif;color:var(--ink);position:relative}
.stage{position:absolute;left:0;top:0;width:1932px;height:1906px;transform:scale(0.621118);transform-origin:0 0}
.screen{position:absolute;background:var(--page);width:825px;overflow:hidden}
.screen--tools{left:106px;top:86px;height:727px}
.screen--detail{left:1002px;top:86px;width:824px;height:1485px}
.screen--survey{left:106px;top:895px;height:924px}

/* header */
.app-header{position:absolute;left:0;top:0;right:0;height:56px;background:#fff}
.brand{position:absolute;left:26px;top:14px;color:var(--ink);font-weight:500;line-height:1}
.brand__name{display:block;font-size:13px;letter-spacing:.6px}
.brand__by{display:block;font-size:7px;margin:3px 0 0 40px}
.main-nav{position:absolute;left:272px;top:0;height:56px;display:flex;align-items:center;gap:22px;font-size:9.5px;color:#3a3a55}
.main-nav span{display:flex;align-items:center;gap:4px}
.nav-ico{width:8px;height:8px;fill:#3a3a55}
.header-tools{position:absolute;left:672px;top:0;height:56px;display:flex;align-items:center;gap:10px;font-size:8.5px;font-weight:500}
.avatar{width:20px;height:20px;border-radius:50%;background:linear-gradient(#5a5a5a,#2c2c2c);margin-left:4px}

/* footer */
.app-footer{position:absolute;left:0;right:0;height:31px;background:var(--footer);color:#fff;font-size:9.5px;display:flex;align-items:center;justify-content:center}
.app-footer small{position:absolute;right:26px;font-size:7px}

/* type */
.page-title{position:absolute;left:0;right:0;text-align:center;font-size:20px;font-weight:500}
.section-title{position:absolute;left:0;right:0;text-align:center;font-size:13px;font-weight:500}
.lead{position:absolute;text-align:center;font-size:9px;line-height:16px;color:var(--muted)}
.lead a{color:var(--green);text-decoration:underline}

/* tool cards */
.tool-card{position:absolute;width:371px;height:148px;background:var(--card);border-radius:10px;display:flex;align-items:center;padding:0 18px 0 13px}
.tool-card--active{box-shadow:0 4px 18px rgba(0,0,0,.12)}
.illus{background:radial-gradient(circle at 55% 55%,var(--green-mid),var(--green-soft) 60%,transparent 72%);border-radius:45%}
.tool-card .illus{width:115px;height:100px;flex:none}
.tool-card__body{margin-left:17px}
.tool-card h3{font-size:13px;font-weight:500;margin-bottom:9px}
.tool-card p{font-size:9px;line-height:15.5px;color:var(--muted);margin-bottom:12px}
.btn{display:inline-flex;align-items:center;gap:6px;background:var(--green);color:#fff;font-size:9.5px;font-weight:500;border-radius:14px;height:24px;padding:0 11px}
.btn i{width:8px;height:8px;border-radius:50%;background:#fff;position:relative}
.btn i::after{content:"";position:absolute;left:2px;top:2.2px;border-left:4px solid var(--green);border-top:2px solid transparent;border-bottom:2px solid transparent}

/* form card */
.form-card{position:absolute;left:25px;top:201px;width:772px;height:323px;background:var(--card);border-radius:10px}
.form-card .illus{position:absolute;left:58px;top:93px;width:270px;height:208px}
.field-label{position:absolute;left:387px;font-size:9.5px;font-weight:500}
.field{position:absolute;left:387px;width:360px;height:35px;border-radius:18px;background:var(--field);font-size:8px;color:var(--faint);padding:13px 18px}
.form-note{position:absolute;left:387px;top:251px;font-size:9px}

/* accordion */
.accordion{position:absolute;width:372px;height:38px;background:var(--card);border-radius:4px;display:flex;align-items:center;justify-content:space-between;padding:0 24px;font-size:10.5px;font-weight:500}
.chev{width:10px;height:10px}

/* highlight */
.highlight{position:absolute;left:25px;top:809px;width:772px;height:131px;background:var(--green);border-radius:10px;color:#fff;text-align:center}
.highlight h3{font-size:14px;font-weight:500;margin-top:20px}
.highlight p{font-size:9px;line-height:15.5px;margin:11px 70px 0}
.highlight a{color:#fff;font-weight:700;text-decoration:underline}

/* hurdles */
.hurdle{position:absolute;left:50px;width:740px}
.hurdle__icon{position:absolute;left:0;top:0;width:56px;height:56px;border-radius:50%;background:var(--green)}
.hurdle__icon::after{content:"";position:absolute;left:17px;top:17px;width:22px;height:22px;border:2px solid #fff;border-radius:50%}
.hurdle__text{margin-left:78px;margin-top:-8px}
.hurdle h4{font-size:10.5px;font-weight:500;margin-bottom:10px}
.hurdle p{font-size:9px;line-height:16px;color:var(--muted)}

/* survey */
.tab{position:absolute;top:212px;width:95px;height:27px;border-radius:14px;color:#fff;font-size:9.5px;font-weight:500;display:flex;align-items:center;justify-content:center}
.tab--on{left:310px;background:var(--green)}
.tab--off{left:420px;background:var(--tab-off)}
.question{position:absolute;left:138px;width:560px}
.question h5{font-size:10.5px;font-weight:400;margin-bottom:14px}
.options{position:relative;height:12px;font-size:9px;color:var(--faint)}
.options span{position:absolute;top:0;display:flex;align-items:center;gap:5px}
.options span::before{content:"";width:7px;height:7px;border:1px solid #9a9aa2;border-radius:50%}
.send{position:absolute;left:377px;top:820px;width:70px;height:25px;border-radius:13px;background:var(--green);color:#fff;font-size:10px;font-weight:500;display:flex;align-items:center;justify-content:center}
</style>
</head>
<body>
<div class="stage">

<!-- Tools overview -->
<section class="screen screen--tools">
  <header class="app-header">
    <div class="brand"><span class="brand__name">CREW LIFTERS</span><span class="brand__by">by Velkor Institute</span></div>
    <nav class="main-nav">
      <span><svg class="nav-ico" viewBox="0 0 8 8"><rect width="3.5" height="3.5"/><rect x="4.5" width="3.5" height="3.5"/><rect y="4.5" width="3.5" height="3.5"/><rect x="4.5" y="4.5" width="3.5" height="3.5"/></svg>Dashboard</span>
      <span><svg class="nav-ico" viewBox="0 0 8 8"><circle cx="4" cy="4" r="3.5"/></svg>Tools</span>
      <span><svg class="nav-ico" viewBox="0 0 8 8"><rect y="1" width="8" height="6" rx="1"/></svg>About us</span>
      <span><svg class="nav-ico" viewBox="0 0 8 8"><rect x="1" width="6" height="8" rx="1"/></svg>Pages ⌄</span>
      <span><svg class="nav-ico" viewBox="0 0 8 8"><ellipse cx="4" cy="3.5" rx="4" ry="3"/></svg>Feedback?</span>
    </nav>
    <div class="header-tools">
      <svg width="12" height="12" viewBox="0 0 12 12"><circle cx="6" cy="6" r="4.5" fill="none" stroke="#2a8bd8" stroke-width="1.6"/><circle cx="6" cy="6" r="1.6" fill="#2a8bd8"/></svg>
      <svg width="12" height="12" viewBox="0 0 12 12"><circle cx="6" cy="6" r="5" fill="var(--green)"/></svg>
      <div class="avatar" role="img" aria-label="User avatar"></div>
      <span>John Doe ⌄</span>
    </div>
  </header>

  <h1 class="page-title" style="top:90px">Free tools to strengthen your teams</h1>
  <p class="lead" style="left:90px;width:645px;top:126px">To make your team - and organization - better, you first need to map out how things are now. Our tools give you insight into the health of your team and the culture of the organization. With the results in hand, you can start improving your team and your organization. Each tool gives you useful tips and tricks to make improvements. Are you stuck? We are happy to help you!</p>

  <article class="tool-card tool-card--active" style="left:26px;top:201px">
    <div class="illus" role="img" aria-label="Illustration of colleagues building together"></div>
    <div class="tool-card__body">
      <h3>Psychological safety</h3>
      <p>Measure the psychological safety in your team completely anonymously.</p>
      <span class="btn">Go to the questionnaire <i></i></span>
    </div>
  </article>
  <article class="tool-card" style="left:425px;top:201px">
    <div class="illus" role="img" aria-label="Illustration of colleagues shaking hands in an office"></div>
    <div class="tool-card__body">
      <h3>Brandt Culture Scan</h3>
      <p>With this tool you visualize the general culture of your organization. Is it mainly a Control, Competence, Collaboration or Cultivation culture?</p>
      <span class="btn">Go to the questionnaire <i></i></span>
    </div>
  </article>
  <article class="tool-card" style="left:226px;top:375px">
    <div class="illus" role="img" aria-label="Illustration of a developer at a desk with code screens"></div>
    <div class="tool-card__body">
      <h3>Developer Culture Test</h3>
      <p>Measure the Development culture in your organization. Do you have what it takes to attract and retain talent?</p>
      <span class="btn">Go to the questionnaire <i></i></span>
    </div>
  </article>

  <h2 class="page-title" style="top:560px">Interventions</h2>
  <p class="lead" style="left:82px;width:660px;top:596px;line-height:17.5px">Using these tools is a first step towards improvement. The tools give you insight with which you can apply suitable interventions. For example, working on the psychological safety of a team by getting to know each other better (do an escape room together, or create one yourself ) and rewarding interpersonal risks <a>(holding a failure party).</a></p>

  <footer class="app-footer" style="top:696px">2021 Copyright - Crewlifters | All Rights Reserved<small>C37</small></footer>
</section>

<!-- Tool detail -->
<section class="screen screen--detail">
  <header class="app-header">
    <div class="brand"><span class="brand__name">CREW LIFTERS</span><span class="brand__by">by Velkor Institute</span></div>
    <nav class="main-nav">
      <span><svg class="nav-ico" viewBox="0 0 8 8"><rect width="3.5" height="3.5"/><rect x="4.5" width="3.5" height="3.5"/><rect y="4.5" width="3.5" height="3.5"/><rect x="4.5" y="4.5" width="3.5" height="3.5"/></svg>Dashboard</span>
      <span><svg class="nav-ico" viewBox="0 0 8 8"><circle cx="4" cy="4" r="3.5"/></svg>Tools</span>
      <span><svg class="nav-ico" viewBox="0 0 8 8"><rect y="1" width="8" height="6" rx="1"/></svg>About us</span>
      <span><svg class="nav-ico" viewBox="0 0 8 8"><rect x="1" width="6" height="8" rx="1"/></svg>Pages ⌄</span>
      <span><svg class="nav-ico" viewBox="0 0 8 8"><ellipse cx="4" cy="3.5" rx="4" ry="3"/></svg>Feedback?</span>
    </nav>
    <div class="header-tools">
      <svg width="12" height="12" viewBox="0 0 12 12"><circle cx="6" cy="6" r="4.5" fill="none" stroke="#2a8bd8" stroke-width="1.6"/><circle cx="6" cy="6" r="1.6" fill="#2a8bd8"/></svg>
      <svg width="12" height="12" viewBox="0 0 12 12"><circle cx="6" cy="6" r="5" fill="var(--green)"/></svg>
      <div class="avatar" role="img" aria-label="User avatar"></div>
      <span>John Doe ⌄</span>
    </div>
  </header>

  <h1 class="page-title" style="top:90px">Psychological safety</h1>
  <p class="lead" style="left:82px;width:660px;top:126px">Psychological safety is just about the most important thing there is in a team. Research at Nordvale , among others, shows that this factor contributes the most to the performance of a team. Read below what exactly psychological safety is, or create your own questionnaire right away and measure how the psychological safety of your team is doing.</p>

  <div class="form-card">
    <h3 class="section-title" style="top:24px">Receive the link to the questionnaire</h3>
    <p class="lead" style="left:130px;width:512px;top:45px;line-height:15px">Here you will receive the link to your own team questionnaire. Enter your team name and your email address. We only use your email address to send you the link to the survey.</p>
    <div class="illus" role="img" aria-label="Illustration of a woman placing charts on a dashboard board"></div>
    <label class="field-label" style="top:104px">Team Name</label>
    <div class="field" style="top:125px">Team Awesome</div>
    <label class="field-label" style="top:174px">E-mail</label>
    <div class="field" style="top:195px">janine@domain.org</div>
    <p class="form-note">We will never distribute your email address</p>
    <span class="btn" style="position:absolute;left:387px;top:269px;height:28px;padding:0 20px">Generate Link <i></i></span>
  </div>

  <h2 class="section-title" style="top:579px">What is Psychological Safety?</h2>
  <p class="lead" style="left:85px;width:654px;top:604px">You probably recognize it: you work with or in a team where things play a role. You immediately feel tension, a pink elephant in the room. But nobody dares to say anything. People do not address each other. Own opinions are not given and team members react defensively. Sometimes it is more difficult to recognize. For example, when everything seems to be happy, but behind each other's backs are looked at each other in a skewed way. The harmonious team that does not dare to take risks. In these cases there is no psychological safety. Team members are engaged in self-preservation and the team is not going to fly. It is therefore very important that there is a high psychological safety in your team!</p>

  <div class="accordion" style="left:25px;top:714px">What is Psychological Safety?<svg class="chev" viewBox="0 0 10 10"><circle cx="5" cy="5" r="5" fill="var(--green)"/><path d="M3 4.2 5 6.2 7 4.2" fill="none" stroke="#fff" stroke-width="1.3"/></svg></div>
  <div class="accordion" style="left:425px;top:714px">How do you improve psychological safety?<svg class="chev" viewBox="0 0 10 10"><circle cx="5" cy="5" r="5" fill="var(--green)"/><path d="M3 4.2 5 6.2 7 4.2" fill="none" stroke="#fff" stroke-width="1.3"/></svg></div>

  <div class="highlight">
    <h3>Scientifically validated basis</h3>
    <p>Our tool is based on the <a>questionnaire developed by Halden professor Mira Ostrand</a> - scientifically sound! With our tool you quickly measure how your team assesses its social climate. Seven questions provide an overall picture of psychological safety in the team. Enter your team name and e-mail address above and you will receive a link to the questionnaire. This link is especially for your team. Expose the psychological safety of your team and take steps to improve it.</p>
  </div>

  <h2 class="section-title" style="top:995px">What about psychological safety if you work online and therefore remotely?</h2>
  <p class="lead" style="left:90px;width:644px;top:1021px">Since Corona, we have been working a lot - and perhaps mainly - online, remotely, together. And that does something to psychological safety. How do you ensure that an environment of trust is created online? There are 3 hurdles to overcome: uncertainty, unfamiliarity and transparency.</p>

  <div class="hurdle" style="top:1085px">
    <div class="hurdle__icon" role="img" aria-label="Uncertainty icon"></div>
    <div class="hurdle__text"><h4>Uncertainty</h4><p>These are uncertain times. And we would like to combat uncertainty, which is very natural behavior. We do this by on the one hand putting our energy into self-preservation and on the other hand by carrying the burden together.To begin with, you cannot spend energy that you spend on self-preservation coming up with creative solutions to deal with that uncertainty. You are building a defense line, as long as you come out unharmed. So that does not help in creating psychological safety. You notice that it is more difficult to discuss sensitive topics online. Meetings are often used very deliberately and quickly leave no room for sharing concerns and other emotional issues. And video calling and chatting are also a bump in my experience. Do you want to build on psychological safety? Then this bump must be resolved.</p></div>
  </div>
  <div class="hurdle" style="top:1228px">
    <div class="hurdle__icon" role="img" aria-label="Unfamiliarity icon"></div>
    <div class="hurdle__text"><h4>Unfamiliarity</h4><p>A second obstacle is unfamiliarity with each other. We are increasingly in the situation that we have never met new colleagues in person. And I don't know how you feel about it, but I still find it easier to get to know someone in person. Not that that doesn't work online. But that requires conscious handling of your online meetings. To build psychological safety you need to know what you can expect from each other. By getting to know each other well, you create this understanding, which is less automatic online.</p></div>
  </div>
  <div class="hurdle" style="top:1340px">
    <div class="hurdle__icon" role="img" aria-label="Less transparency icon"></div>
    <div class="hurdle__text"><h4>Less transparency</h4><p>It is less easy to see what everyone is doing from a distance. But more importantly: how people think about things. Where you quickly sense the undertone in a group that is physically together and notice what is not being said, it is much more difficult online. The result is that it is difficult to feel whether you can take a personal risk or not.</p></div>
  </div>

  <footer class="app-footer" style="top:1454px">2021 Copyright - Crewlifters | All Rights Reserved<small>C37</small></footer>
</section>

<!-- Questionnaire -->
<section class="screen screen--survey">
  <header class="app-header">
    <div class="brand"><span class="brand__name">CREW LIFTERS</span><span class="brand__by">by Velkor Institute</span></div>
    <nav class="main-nav">
      <span><svg class="nav-ico" viewBox="0 0 8 8"><rect width="3.5" height="3.5"/><rect x="4.5" width="3.5" height="3.5"/><rect y="4.5" width="3.5" height="3.5"/><rect x="4.5" y="4.5" width="3.5" height="3.5"/></svg>Dashboard</span>
      <span><svg class="nav-ico" viewBox="0 0 8 8"><circle cx="4" cy="4" r="3.5"/></svg>Tools</span>
      <span><svg class="nav-ico" viewBox="0 0 8 8"><rect y="1" width="8" height="6" rx="1"/></svg>About us</span>
      <span><svg class="nav-ico" viewBox="0 0 8 8"><rect x="1" width="6" height="8" rx="1"/></svg>Pages ⌄</span>
      <span><svg class="nav-ico" viewBox="0 0 8 8"><ellipse cx="4" cy="3.5" rx="4" ry="3"/></svg>Feedback?</span>
    </nav>
    <div class="header-tools">
      <svg width="12" height="12" viewBox="0 0 12 12"><circle cx="6" cy="6" r="4.5" fill="none" stroke="#2a8bd8" stroke-width="1.6"/><circle cx="6" cy="6" r="1.6" fill="#2a8bd8"/></svg>
      <svg width="12" height="12" viewBox="0 0 12 12"><circle cx="6" cy="6" r="5" fill="var(--green)"/></svg>
      <div class="avatar" role="img" aria-label="User avatar"></div>
      <span>John Doe ⌄</span>
    </div>
  </header>

  <h1 class="page-title" style="top:89px;font-size:22px">Psychological safety of John Doe</h1>
  <div class="accordion" style="left:26px;top:139px;width:371px;height:37px">What is Psychological Safety?<svg class="chev" viewBox="0 0 10 10"><circle cx="5" cy="5" r="5" fill="var(--green)"/><path d="M3 4.2 5 6.2 7 4.2" fill="none" stroke="#fff" stroke-width="1.3"/></svg></div>
  <div class="accordion" style="left:425px;top:139px;width:372px;height:37px">How do you improve psychological safety?<svg class="chev" viewBox="0 0 10 10"><circle cx="5" cy="5" r="5" fill="var(--green)"/><path d="M3 4.2 5 6.2 7 4.2" fill="none" stroke="#fff" stroke-width="1.3"/></svg></div>

  <span class="tab tab--on">Your answer</span>
  <span class="tab tab--off">Results (0)</span>

  <h2 class="section-title" style="top:270px;font-size:14px">How do you rate your team climate?</h2>
  <p class="lead" style="left:118px;width:590px;top:296px">With this questionnaire you can determine your assessment of the psychological safety of your team. Answer these 7 questions and view the answers of your team members in the Answers tab . All answers remain anonymous !</p>

  <div class="question" style="top:353px"><h5>1) When someone on the team makes a mistake, it is often used against him or her</h5><div class="options"><span style="left:25px">Strongly disagree</span><span style="left:170px">Disagree</span><span style="left:279px">Neutral</span><span style="left:383px">once</span><span style="left:476px">strongly agree</span></div></div>
  <div class="question" style="top:418px"><h5>2) In this team it is easy to discuss sensitive topics and problems</h5><div class="options"><span style="left:25px">Strongly disagree</span><span style="left:170px">Disagree</span><span style="left:279px">Neutral</span><span style="left:383px">once</span><span style="left:476px">strongly agree</span></div></div>
  <div class="question" style="top:483px"><h5>3) In this team, people are sometimes rejected because they are different</h5><div class="options"><span style="left:25px">Strongly disagree</span><span style="left:170px">Disagree</span><span style="left:279px">Neutral</span><span style="left:383px">once</span><span style="left:476px">strongly agree</span></div></div>
  <div class="question" style="top:548px"><h5>4) It is absolutely safe to take a risk on this team</h5><div class="options"><span style="left:25px">Strongly disagree</span><span style="left:170px">Disagree</span><span style="left:279px">Neutral</span><span style="left:383px">once</span><span style="left:476px">strongly agree</span></div></div>
  <div class="question" style="top:613px"><h5>5) It is difficult to ask others in the team for help</h5><div class="options"><span style="left:25px">Strongly disagree</span><span style="left:170px">Disagree</span><span style="left:279px">Neutral</span><span style="left:383px">once</span><span style="left:476px">strongly agree</span></div></div>
  <div class="question" style="top:678px"><h5>6) No one on this team consciously acts in a way that undermines my efforts</h5><div class="options"><span style="left:25px">Strongly disagree</span><span style="left:170px">Disagree</span><span style="left:279px">Neutral</span><span style="left:383px">once</span><span style="left:476px">strongly agree</span></div></div>
  <div class="question" style="top:743px"><h5>7) Members of this team value and respect each other's contributions</h5><div class="options"><span style="left:25px">Strongly disagree</span><span style="left:170px">Disagree</span><span style="left:279px">Neutral</span><span style="left:383px">once</span><span style="left:476px">strongly agree</span></div></div>

  <span class="send">Send</span>
  <footer class="app-footer" style="top:893px">2021 Copyright - Crewlifters | All Rights Reserved<small>C37</small></footer>
</section>

</div>
</body>
</html>
```